Professional Business Card for Commercial Cleaning Company

We need a business card that represents our commercial janitorial cleaning company and represent several brands for our company so we do not want to highlight the logo too much. We want something that says we are professional.
Notes:No website or address as we have many locations and many websites and companies under our corporate name of "Brightvale Holdings, LLC" . Every time we hand a customer a business card they have contacted us via another brand we own but we don't want to have 21 business cards so we want to not focus on Brightvale Holdings, LLC too much since people will automatically ask "What is Brightvale Holdings, LLC" Example: Noodle Barn and Wrap Lantern restaurants are owned by "Zest! Brands" is the corporation name. Same principle here. Except we do not advertise at this time that all of our brands are connected. Hope this helps.
Target Market(s)
Commercial Cleaning
Industry/Entity Type
Janitorial Service
Contact Information for Business Card
Milo Jarvis
Business Development
555-382-9047
sales@brightvaleholdingsllc.example
Requirements
Must have
- Logo with contact information, need to be able to easily edit contact info for others in my office.
Nice to have
- Professional Image. Like to see a colorful bold look and a more standard business card look.
Should not have
- Any type of cleaning icons, tools, people or water.

```html
<!DOCTYPE html>
<html lang="en">
<head>
<meta charset="utf-8">
<title>Brightvale Holdings, LLC — Business Card</title>
<link href="https://fonts.googleapis.com/css2?family=Roboto:wght@400;500;700&display=swap" rel="stylesheet">
<style>
  :root {
    --navy: #003a7a;
    --green: #69a834;
    --white: #ffffff;
    --stage: #c4c4c4;
    --shadow: rgba(0, 0, 0, 0.25);
  }
  * { margin: 0; padding: 0; box-sizing: border-box; }
  html, body {
    width: 1200px;
    height: 1200px;
    overflow: hidden;
    background: var(--stage);
    font-family: "Roboto", Arial, sans-serif;
  }
  .card {
    position: absolute;
    left: 217px;
    width: 800px;
    height: 460px;
    box-shadow: 0 3px 8px var(--shadow);
    overflow: hidden;
    background: var(--white);
  }
  .card--front { top: 112px; }
  .card--back { top: 637px; }
  .card__band {
    position: absolute;
    left: 0; right: 0; top: 0;
    height: 262px;
    background: var(--navy);
  }
  .card__rule {
    position: absolute;
    left: 0; right: 0; top: 262px;
    height: 10px;
    background: var(--green);
  }
  .contact {
    position: absolute;
    left: 40px;
    top: 56px;
    color: var(--white);
  }
  .contact__name { font-size: 30px; font-weight: 700; line-height: 36px; }
  .contact__role { font-size: 20px; font-weight: 500; line-height: 26px; }
  .contact__list { list-style: none; margin-top: 16px; }
  .contact__item {
    display: flex;
    align-items: center;
    gap: 10px;
    font-size: 19px;
    line-height: 26px;
  }
  .contact__icon { width: 18px; height: 18px; flex: none; }
  .brand-name {
    position: absolute;
    color: var(--navy);
    font-weight: 700;
    white-space: nowrap;
    letter-spacing: -0.3px;
  }
  .card--front .brand-name { right: 52px; top: 340px; font-size: 36px; }
  .card--back .brand-name {
    left: 0; right: 0; top: 206px;
    text-align: center;
    font-size: 44px;
  }
</style>
</head>
<body>
  <section class="card card--front">
    <div class="card__band"></div>
    <div class="card__rule"></div>
    <div class="contact">
      <p class="contact__name">Milo Jarvis</p>
      <p class="contact__role">Business Development</p>
      <ul class="contact__list">
        <li class="contact__item">
          <svg class="contact__icon" viewBox="0 0 18 18" aria-hidden="true">
            <rect x="4" y="0.8" width="10" height="16.4" rx="1.6" fill="none" stroke="#ffffff" stroke-width="1.6"/>
            <rect x="5.6" y="3" width="6.8" height="10.5" fill="#ffffff"/>
          </svg>
          555-382-9047
        </li>
        <li class="contact__item">
          <svg class="contact__icon" viewBox="0 0 18 18" aria-hidden="true">
            <rect x="1.5" y="4" width="15" height="11" fill="#ffffff"/>
            <path d="M1.5,4 L9,10 L16.5,4" fill="none" stroke="#003a7a" stroke-width="1.3"/>
          </svg>
          sales@brightvaleholdingsllc.example
        </li>
      </ul>
    </div>
    <p class="brand-name">Brightvale Holdings, LLC</p>
  </section>

  <section class="card card--back">
    <p class="brand-name">Brightvale Holdings, LLC</p>
  </section>
</body>
</html>
```